VORN - Business cards

Business card to be created for Commercial sales staff

Target Market(s)

Commercial businesses

Industry/Entity Type

Commercial

Contact Information for Business Card

Look professional. For commercial clients

Colors
ffffff

Requirements
Must have
• - Vorn Logo
• - Commercial sales staff as postion
• - room for commerical sales manager role
• - person name and their mobile number
• - Website : vornelectrical.com.au
Nice to have
• White background.
• On back of business card just have the logo no other information
Should not have
• Should only have white background on front of card.

```html
<!DOCTYPE html>
<html lang="en">
<head>
<meta charset="utf-8">
<title>VORN – Business Cards</title>
<link rel="stylesheet" href="https://fonts.googleapis.com/css2?family=Jost:wght@300;400;700&display=swap">
<style>
  :root {
    --page-bg: #ececec;
    --card-black: #0b0b0b;
    --panel-black: #161616;
    --gold: #d4a72c;
    --gold-soft: #b8922a;
  }
  * { margin: 0; padding: 0; box-sizing: border-box; }
  html, body {
    width: 1200px;
    height: 800px;
    overflow: hidden;
    background: var(--page-bg);
    font-family: "Jost", sans-serif;
  }
  .sheet {
    position: relative;
    width: 1200px;
    height: 800px;
    display: flex;
    align-items: center;
    justify-content: center;
    gap: 60px;
  }
  .card {
    position: relative;
    width: 520px;
    height: 300px;
    background: var(--card-black);
    overflow: hidden;
  }

  /* Back of card: brand name only */
  .card-back {
    display: flex;
    align-items: center;
    justify-content: center;
  }
  .brand {
    display: flex;
    align-items: center;
    gap: 14px;
  }
  .brand-dot {
    width: 34px;
    height: 34px;
    border-radius: 50%;
    background: var(--gold);
  }
  .brand-name {
    font-weight: 700;
    font-size: 56px;
    letter-spacing: 2px;
    color: var(--gold);
    line-height: 1;
  }

  /* Front of card: person and contact details */
  .identity {
    position: absolute;
    top: 78px;
    left: 0;
    right: 0;
    text-align: center;
  }
  .person-name {
    font-weight: 300;
    font-size: 36px;
    letter-spacing: 12px;
    color: var(--gold);
    line-height: 1;
    padding-left: 12px;
  }
  .person-role {
    margin-top: 10px;
    font-weight: 400;
    font-size: 9px;
    letter-spacing: 3.2px;
    color: var(--gold);
    padding-left: 3px;
  }
  .contacts {
    position: absolute;
    left: 0;
    right: 0;
    bottom: 0;
    height: 126px;
    display: grid;
    grid-template-columns: repeat(3, 1fr);
  }
  .contact {
    position: relative;
    display: flex;
    flex-direction: column;
  }
  .contact + .contact::before {
    content: "";
    position: absolute;
    left: 0;
    bottom: 12px;
    height: 32px;
    width: 1px;
    background: var(--gold-soft);
  }
  .contact-panel {
    height: 72px;
    background: var(--panel-black);
    display: flex;
    align-items: center;
    justify-content: center;
  }
  .contact-panel svg { width: 16px; height: 16px; fill: var(--gold); }
  .contact-text {
    flex: 1;
    display: flex;
    align-items: center;
    justify-content: center;
    font-size: 9px;
    letter-spacing: 1.6px;
    color: var(--gold);
  }
</style>
</head>
<body>
  <main class="sheet">
    <section class="card card-back" aria-label="Card back">
      <div class="brand">
        <span class="brand-dot"></span>
        <span class="brand-name">VORN</span>
      </div>
    </section>

    <section class="card card-front" aria-label="Card front">
      <div class="identity">
        <h1 class="person-name">JOHN DOE</h1>
        <p class="person-role">COMMERCIAL SALES STAFF</p>
      </div>
      <div class="contacts">
        <div class="contact">
          <div class="contact-panel">
            <svg viewBox="0 0 24 24" aria-hidden="true"><path d="M6.6 10.8c1.4 2.8 3.8 5.1 6.6 6.6l2.2-2.2c.3-.3.7-.4 1-.2 1.1.4 2.3.6 3.6.6.6 0 1 .4 1 1V20c0 .6-.4 1-1 1C10.6 21 3 13.4 3 4c0-.6.4-1 1-1h3.5c.6 0 1 .4 1 1 0 1.3.2 2.5.6 3.6.1.3 0 .7-.2 1z"/></svg>
          </div>
          <p class="contact-text">000.1234.5678</p>
        </div>
        <div class="contact">
          <div class="contact-panel">
            <svg viewBox="0 0 24 24" aria-hidden="true"><path d="M3 5h18v14H3z M3 5l9 7 9-7" fill="none" stroke="#d4a72c" stroke-width="0"/><path d="M3 6.2V19h18V6.2l-9 7zM3.8 5h16.4L12 11.4z"/></svg>
          </div>
          <p class="contact-text">johndoe@email.com</p>
        </div>
        <div class="contact">
          <div class="contact-panel">
            <svg viewBox="0 0 24 24" aria-hidden="true"><path d="M12 18.5a2 2 0 1 1 0 .01zM6.5 13.5a7.8 7.8 0 0 1 11 0l-1.6 1.6a5.5 5.5 0 0 0-7.8 0zM3 10a12.7 12.7 0 0 1 18 0l-1.6 1.6a10.4 10.4 0 0 0-14.8 0z"/></svg>
          </div>
          <p class="contact-text">vornelectrical.com.au</p>
        </div>
      </div>
    </section>
  </main>
</body>
</html>
```